Stationary pack for BrightVane

BrightVane is a recently establish Solar brokerage company based in Australia. We have a number of sales staff who provide advice and guidance to both residential and commercial customers regarding solar systems (solar hot water and solar panels.)

In addition to our brokerage services we are also developing software for the solar industry, which will be used to automate the solar system install process. This system will be used by other companies in the solar industry including installers, wholesalers and government departments.

We are after a stationary pack that consists of the following: Business cards, compliments slip and letter head.

The EPS, AI, PNG etc files for the logo are attached.

For the business card:
The name and logo of the company need to be clearly visible. On the back of the business cards, we would like the logo. I am happy for you to split the image part of the logo from the text if you think it would look better a different way.

I would like the business cards to be easily readable with the following information on the front:
Name
(Please leave room for titles for the future – eg Sales Advisor.)
Mobile
Office
Email
Address
ABN

Letter heads:
I would prefer the address to be at the top

Compliments slips:
Only need to be one sided

Target Market(s)

BrightVane provides services to both residential and commercial customers. Our customers will be environmentally conscious.

Industry/Entity Type

Residential

Requirements
Must have
• Business cards must have the logo on the back.

```html
<!DOCTYPE html>
<html lang="en">
<head>
<meta charset="utf-8">
<title>BrightVane Letterhead</title>
<link rel="stylesheet" href="https://fonts.googleapis.com/css2?family=Nunito:wght@800&family=Inconsolata:wght@400&display=swap">
<style>
  :root {
    --backdrop: #dcdcdc;
    --paper: #ffffff;
    --brand-green: #5a9e3a;
    --wash-green: #f1f5ec;
    --wash-green-soft: #f6f9f2;
    --detail-grey: #9a9a9a;
  }
  * { margin: 0; padding: 0; box-sizing: border-box; }
  html, body {
    width: 1200px;
    height: 900px;
    overflow: hidden;
    background: var(--backdrop);
  }
  .canvas {
    position: relative;
    width: 1200px;
    height: 900px;
  }
  .letterhead {
    position: absolute;
    left: 290px;
    top: 20px;
    width: 600px;
    height: 854px;
    background: var(--paper);
    overflow: hidden;
  }
  .letterhead__wash {
    position: absolute;
    inset: 0;
    width: 600px;
    height: 854px;
  }
  .masthead {
    position: absolute;
    top: 28px;
    left: 0;
    width: 100%;
    text-align: center;
  }
  .masthead__dot {
    display: block;
    width: 40px;
    height: 40px;
    margin: 0 auto 6px;
    border-radius: 50%;
    background: var(--brand-green);
  }
  .masthead__name {
    font-family: "Nunito", sans-serif;
    font-weight: 800;
    font-size: 24px;
    line-height: 1;
    color: var(--brand-green);
    letter-spacing: -0.3px;
  }
  .masthead__details {
    margin-top: 8px;
    font-family: "Inconsolata", monospace;
    font-size: 10px;
    line-height: 16px;
    color: var(--detail-grey);
    letter-spacing: 0.6px;
  }
</style>
</head>
<body>
  <div class="canvas">
    <div class="letterhead">
      <svg class="letterhead__wash" viewBox="0 0 600 854" role="img" aria-label="Soft pale green decorative wash sweeping down the right side of the page">
        <defs>
          <linearGradient id="washFade" x1="0" y1="0" x2="1" y2="1">
            <stop offset="0" stop-color="var(--wash-green)"/>
            <stop offset="1" stop-color="var(--wash-green-soft)"/>
          </linearGradient>
        </defs>
        <path d="M346 0 C 340 300, 280 600, 166 854 L600 854 L600 0 Z" fill="url(#washFade)"/>
      </svg>
      <header class="masthead">
        <span class="masthead__dot"></span>
        <div class="masthead__name">BrightVane</div>
        <div class="masthead__details">
          <div>27 Wattle Rd · Bayside · 3186</div>
          <div>0412 305 118</div>
        </div>
      </header>
    </div>
  </div>
</body>
</html>
```